Almond butter sachet and jar for new brand called Fenwick’s Pantry

Design for the front and back of a Almond butter sachet and jar, premium design aimed at the fitness market but still approachable for non gym goers.
The Brand name is Fenwick’s Pantry,
Martin Hale is the founder and a michelin starred chef. We want this to stand out from the crowd as a luxury, natural product for use in the gym as well as on the go, we like the premium look of black as a base colour and red colours as they don’t exist in the market, however they can be a little too bold, Our product is natural with no additives, it is vegan, paleo, keto, friendly, plant based and gluten free and only uses hi-Oleic Nuts and no sweetness or palm oil.
Pictures below of the dot&seed sachet and jar are the exact same style as our sachet and jar. The other product is one we really like the look of which is aimed at the fitness market, we don’t want to be the same but almost a hybrid of the two. Our target market however is the high end fitness community, especially with the sachet.

Target Market(s)

Health and Fitness

Requirements
Must have
• High end look and feel,
Nice to have
• Any unique touches to make it stand out from the crowd

```html
<!DOCTYPE html>
<html lang="en">
<head>
<meta charset="utf-8">
<title>Fenwick’s Pantry Almond Butter – Jar Label and Pouch Front</title>
<link rel="stylesheet" href="https://fonts.googleapis.com/css2?family=Amatic+SC:wght@700&family=Lora:wght@400;600&display=swap">
<style>
  :root {
    --stage: #8a8a8a;
    --paper: #eceae7;
    --paper-shade: #dcd9d5;
    --orange: #f7731c;
    --orange-deep: #e8600f;
    --cocoa: #4a2a28;
    --ink: #1c1a1a;
    --almond: #c9734f;
    --almond-shell: #c8a282;
    --white: #ffffff;
  }
  * { margin: 0; padding: 0; box-sizing: border-box; }
  html, body {
    width: 1200px;
    height: 849px;
    overflow: hidden;
    background: var(--stage);
  }
  .canvas {
    position: relative;
    width: 1200px;
    height: 849px;
  }
  .jar-label {
    position: absolute;
    left: 150px;
    top: 320px;
    width: 420px;
    height: 380px;
  }
  .pouch-front {
    position: absolute;
    left: 700px;
    top: 48px;
    width: 398px;
    height: 752px;
  }
  .brand-name {
    font-family: "Lora", Georgia, serif;
    font-weight: 600;
  }
  .tagline {
    font-family: "Lora", Georgia, serif;
    font-weight: 400;
    fill: var(--white);
  }
  .product-name {
    font-family: "Amatic SC", "Comic Sans MS", cursive;
    font-weight: 700;
  }
</style>
</head>
<body>
<main class="canvas">

  <!-- Jar label, flat -->
  <svg class="jar-label" viewBox="0 0 420 380" xmlns="http://www.w3.org/2000/svg">
    <defs>
      <clipPath id="jar-clip"><rect width="420" height="380"/></clipPath>
      <radialGradient id="jar-paper" cx="50%" cy="45%" r="70%">
        <stop offset="0" stop-color="var(--paper)"/>
        <stop offset="1" stop-color="var(--paper-shade)"/>
      </radialGradient>
      <linearGradient id="almond-fill" x1="0" y1="0" x2="1" y2="1">
        <stop offset="0" stop-color="var(--almond-shell)"/>
        <stop offset="1" stop-color="var(--almond)"/>
      </linearGradient>
    </defs>
    <g clip-path="url(#jar-clip)">
      <rect class="label-paper" width="420" height="380" fill="url(#jar-paper)"/>
      <circle class="brand-disc" cx="57" cy="60" r="95" fill="var(--orange)"/>
      <path class="tagline-band" d="M0 380 L0 372 Q140 285 420 272 L420 380 Z" fill="var(--orange)"/>

      <ellipse class="almond-cluster" cx="240" cy="80" rx="122" ry="62" fill="url(#almond-fill)"
               role="img" aria-label="Illustration of whole almonds in and out of their shells"/>
      <ellipse class="loose-almond" cx="230" cy="175" rx="22" ry="32" transform="rotate(-15 230 175)" fill="var(--almond)"
               role="img" aria-label="Illustration of a single almond"/>
      <ellipse class="loose-almond" cx="250" cy="250" rx="34" ry="17" transform="rotate(12 250 250)" fill="var(--almond)"
               role="img" aria-label="Illustration of a single almond"/>

      <text class="brand-name" x="0" y="0" font-size="40" fill="var(--cocoa)" transform="translate(92 345) rotate(-90)">Fenwick’s Pantry</text>

      <text class="product-name" x="270" y="190" font-size="40" fill="var(--cocoa)">ALMOND</text>
      <text class="product-name" x="270" y="228" font-size="40" fill="var(--cocoa)">BUTTER</text>

      <text class="tagline" x="164" y="322" font-size="22">Natural Nuttiness</text>
    </g>
  </svg>

  <!-- Pouch front, flat -->
  <svg class="pouch-front" viewBox="0 0 398 752" xmlns="http://www.w3.org/2000/svg">
    <defs>
      <clipPath id="pouch-clip"><rect width="398" height="752" rx="10"/></clipPath>
      <radialGradient id="pouch-paper" cx="50%" cy="40%" r="75%">
        <stop offset="0" stop-color="var(--paper)"/>
        <stop offset="1" stop-color="var(--paper-shade)"/>
      </radialGradient>
      <linearGradient id="pouch-almond-fill" x1="0" y1="0" x2="1" y2="1">
        <stop offset="0" stop-color="var(--almond-shell)"/>
        <stop offset="1" stop-color="var(--almond)"/>
      </linearGradient>
    </defs>
    <g clip-path="url(#pouch-clip)">
      <rect class="pouch-paper" width="398" height="752" fill="url(#pouch-paper)"/>
      <line class="zip-seal" x1="0" y1="78" x2="398" y2="78" stroke="var(--paper-shade)" stroke-width="3"/>
      <circle class="brand-disc" cx="44" cy="196" r="120" fill="var(--orange)"/>
      <path class="tagline-band" d="M0 752 L0 690 Q150 560 398 510 L398 752 Z" fill="var(--orange-deep)"/>

      <ellipse class="almond-cluster" cx="282" cy="328" rx="112" ry="66" fill="url(#pouch-almond-fill)"
               role="img" aria-label="Illustration of whole almonds in and out of their shells"/>
      <ellipse class="loose-almond" cx="286" cy="425" rx="22" ry="38" transform="rotate(-10 286 425)" fill="var(--almond)"
               role="img" aria-label="Illustration of a single almond"/>
      <ellipse class="loose-almond" cx="318" cy="520" rx="34" ry="18" transform="rotate(10 318 520)" fill="var(--almond)"
               role="img" aria-label="Illustration of a single almond"/>

      <text class="brand-name" x="0" y="0" font-size="48" fill="var(--ink)" transform="translate(125 548) rotate(-90)">Fenwick’s Pantry</text>

      <text class="product-name" x="198" y="212" font-size="50" fill="var(--ink)">ALMOND</text>
      <text class="product-name" x="198" y="258" font-size="50" fill="var(--ink)">BUTTER</text>

      <text class="tagline" x="150" y="612" font-size="24" transform="rotate(-4 150 612)">Natural Nuttiness</text>
    </g>
  </svg>

</main>
</body>
</html>
```